High Tech Real Estate Startup needs a business card

We are developing an innovative real estate marketing product based around advanced search and virtual reality.

We talk to people, we need business cards.

Target Market(s)

The target market is technology professionals and realtors.

Contact Information for Business Card

The information to be included will include

Name
Title
Phone Number
E-mail Address
www.quelzo.com

It should use simple iconography for each one of those fields.

Font styles to use
Other font styles liked:
• Co, Jubilat, Avenir

Colors

Designer to choose colors to be used in the design.

Requirements
Must have
• Clean aesthetic,
• Good use of negative space.
• It should use our company logo, shown in the attached file. It is able to use the negative of that logo (coloured font and white background) and I have attached other acceptable accent colours in a swatch file.
Should not have
• Should not be too busy
• No extraneous text (slogans, tag lines etc)

```html
<!DOCTYPE html>
<html lang="en">
<head>
<meta charset="utf-8">
<title>Quelzo Business Card</title>
<link rel="stylesheet" href="https://fonts.googleapis.com/css2?family=Montserrat:wght@300;400;600;700&display=swap">
<style>
  :root {
    --page: #e9e9e7;
    --card-dark: #2b2b2c;
    --card-light: #f7f7f6;
    --teal: #17a3a2;
    --ink: #1d1d1d;
    --muted: #c9c9c9;
    --pattern-a: #343435;
    --pattern-b: #2b2b2c;
  }
  * { box-sizing: border-box; margin: 0; padding: 0; }
  html, body {
    width: 1200px; height: 1021px; overflow: hidden;
    background: var(--page);
    font-family: "Montserrat", sans-serif;
  }
  .canvas { position: relative; width: 1200px; height: 1021px; }
  .card {
    position: absolute;
    width: 560px; height: 320px;
    border-radius: 3px;
    box-shadow: 0 6px 18px rgba(0,0,0,.12);
    overflow: hidden;
  }
  /* Back */
  .card--back { left: 70px; top: 120px; background: var(--card-dark); }
  .card__pattern {
    position: absolute; inset: 0;
    background: radial-gradient(ellipse at 85% 20%, var(--pattern-a), var(--pattern-b) 55%),
                var(--card-dark);
  }
  .card__pattern--left {
    background: radial-gradient(ellipse at 10% 75%, var(--pattern-a), transparent 45%);
  }
  .back-content {
    position: absolute; inset: 0;
    display: flex; flex-direction: column; align-items: center; justify-content: center;
    text-align: center;
  }
  .brand-name {
    color: var(--teal);
    font-weight: 400;
    letter-spacing: .08em;
    white-space: nowrap;
  }
  .brand-name--back { font-size: 20px; margin-bottom: 22px; }
  .tagline-light {
    color: var(--muted); font-weight: 300; font-size: 19px; letter-spacing: .22em;
  }
  .tagline-bold {
    color: #ffffff; font-weight: 700; font-size: 19px; letter-spacing: .2em; margin-top: 2px;
  }
  .website { color: var(--teal); font-size: 13px; font-weight: 600; margin-top: 16px; letter-spacing: .03em; }

  /* Front */
  .card--front { left: 570px; top: 580px; background: var(--card-light); }
  .brand-name--front {
    position: absolute; left: 50px; top: 184px;
    width: 200px; text-align: center;
    font-size: 28px;
  }
  .contact { position: absolute; left: 285px; top: 74px; color: var(--ink); }
  .contact__name { font-size: 28px; font-weight: 400; }
  .contact__title { color: var(--teal); font-size: 15px; margin-top: 2px; }
  .contact__list { list-style: none; margin: 16px 0 0 40px; }
  .contact__item { display: flex; align-items: center; gap: 8px; font-size: 15px; margin-bottom: 12px; white-space: nowrap; }
  .contact__icon { width: 16px; height: 16px; fill: var(--ink); flex: none; }
</style>
</head>
<body>
<main class="canvas">
  <section class="card card--back" aria-label="Card back">
    <div class="card__pattern" role="img" aria-label="Faint constellation line pattern across the dark card"></div>
    <div class="card__pattern card__pattern--left" aria-hidden="true"></div>
    <div class="back-content">
      <p class="brand-name brand-name--back">QUELZO</p>
      <p class="tagline-light">GEEKS AT WORK</p>
      <p class="tagline-bold">HELPING YOU MOVE</p>
      <p class="website">www.quelzo.com</p>
    </div>
  </section>

  <section class="card card--front" aria-label="Card front">
    <p class="brand-name brand-name--front">QUELZO</p>
    <div class="contact">
      <h1 class="contact__name">Your Name</h1>
      <p class="contact__title">Title</p>
      <ul class="contact__list">
        <li class="contact__item">
          <svg class="contact__icon" viewBox="0 0 16 16" aria-hidden="true"><path d="M1 5c0-2 3-3 7-3s7 1 7 3v1.5h-3.5V5H4.5v1.5H1zM3 8h10l1.5 6h-13zM8 9.2a2 2 0 1 0 0 4 2 2 0 0 0 0-4z"/></svg>
          <span>000 000 0000</span>
        </li>
        <li class="contact__item">
          <svg class="contact__icon" viewBox="0 0 16 16" aria-hidden="true"><path d="M1 3h14v10H1zM2 4.2v.6l6 4.2 6-4.2v-.6zM2 6.2V12h12V6.2L8 10.4z"/></svg>
          <span>youremail@quelzo.com</span>
        </li>
      </ul>
    </div>
  </section>
</main>
</body>
</html>
```